Business Cards

Need a neat design for a new business card

Industry/Entity Type

Residential Construction

Contact Information for Business Card

Company Name- KORV Construction Inc.
Owner- Daniel Pruitt
Phone number- (555)270-4418
Email- korvcobuilds@mailbox-example.com
Facebook- www.socialpage-example.com/korvcobuilds

Colors
fefdec

```html
<!DOCTYPE html>
<html lang="en">
<head>
<meta charset="UTF-8">
<title>KORV Construction Inc. — Business Card</title>
<link rel="stylesheet" href="https://fonts.googleapis.com/css2?family=Poppins:wght@300;400&display=swap">
<style>
  :root {
    --backdrop: #dedad3;
    --card-light: #ffffff;
    --card-dark: #040507;
    --ink: #111111;
    --ink-soft: #4a4a4a;
    --ink-muted: #8a8a8a;
    --paper-text: #fefdec;
  }
  * { margin: 0; padding: 0; box-sizing: border-box; }
  html, body {
    width: 1125px;
    height: 1200px;
    overflow: hidden;
    background: var(--backdrop);
    font-family: "Poppins", Arial, sans-serif;
  }
  .canvas {
    position: relative;
    width: 1125px;
    height: 1200px;
  }
  .card {
    position: absolute;
    left: 171px;
    width: 826px;
    height: 471px;
    box-shadow: 0 3px 8px rgba(0,0,0,0.25);
  }
  .card--front { top: 106px; background: var(--card-light); }
  .card--back  { top: 639px; background: var(--card-dark); }

  .contact-frame {
    position: absolute;
    left: 183px;
    top: 170px;
    width: 475px;
    height: 183px;
  }
  .contact-frame svg { position: absolute; left: 0; top: 0; }
  .frame-accent {
    position: absolute;
    left: 227px;
    top: -10px;
    width: 20px;
    height: 20px;
    background: var(--ink);
  }
  .contact-block {
    position: absolute;
    left: 0;
    right: 0;
    top: 40px;
    text-align: center;
  }
  .owner-name {
    font-size: 25px;
    font-weight: 400;
    letter-spacing: 1px;
    color: var(--ink);
    line-height: 30px;
  }
  .owner-title {
    font-size: 17px;
    font-weight: 400;
    color: var(--ink-muted);
    line-height: 26px;
  }
  .contact-line {
    font-size: 16px;
    font-weight: 300;
    color: var(--ink-soft);
    line-height: 26px;
  }
  .contact-line--first { margin-top: 8px; }

  .brand {
    position: absolute;
    inset: 0;
    display: flex;
    align-items: center;
    justify-content: center;
    gap: 30px;
  }
  .brand-square {
    width: 70px;
    height: 70px;
    background: var(--paper-text);
  }
  .brand-name {
    color: var(--paper-text);
    font-weight: 300;
    font-family: "Poppins", Arial, sans-serif;
  }
  .brand-name__main {
    display: block;
    font-size: 84px;
    line-height: 84px;
    letter-spacing: 4px;
  }
  .brand-name__sub {
    display: block;
    font-size: 24px;
    line-height: 34px;
    letter-spacing: 4px;
    margin-top: 6px;
  }
</style>
</head>
<body>
<main class="canvas">
  <section class="card card--front" aria-label="Business card front">
    <div class="contact-frame">
      <svg width="475" height="183" viewBox="0 0 475 183" aria-hidden="true">
        <polyline points="168,1.5 1.5,1.5 1.5,181.5 473.5,181.5 473.5,1.5 308,1.5"
                  fill="none" stroke="var(--ink)" stroke-width="3"/>
      </svg>
      <span class="frame-accent" aria-hidden="true"></span>
      <div class="contact-block">
        <h1 class="owner-name">DANIEL PRUITT</h1>
        <p class="owner-title">Owner</p>
        <p class="contact-line contact-line--first">(555)270-4418 | korvcobuilds@mailbox-example.com</p>
        <p class="contact-line">@korvcobuilds</p>
      </div>
    </div>
  </section>

  <section class="card card--back" aria-label="Business card back">
    <div class="brand">
      <span class="brand-square" aria-hidden="true"></span>
      <p class="brand-name">
        <span class="brand-name__main">KORV</span>
        <span class="brand-name__sub">CONSTRUCTION</span>
      </p>
    </div>
  </section>
</main>
</body>
</html>
```